Radiant Harbor Holdings business card

We are a real estate advisory and investment company. We are specialized in assisting high networth individuals to invest in real estate overseas. We deliver a very personalized service, anticipating all the potential challenges an investor can face, and making it easy and safe for them. We also co-invest with our clients, assuring them that each project will be looked after as it is our own, and at the same time giving them the extra booth on confidence to invest.

We need a business card design. The business card must have a very premium, high-end look, reflecting principles like "commitment", "trust" and "timeless (but contemporary)". We look for long term relationships with our clients, and we grow with their referrals. We are all about conquering the confidence of the clients by always delivering above the expectations performance.

Target Market(s)

High net worth individuals.

Industry/Entity Type

Real Estate

Contact Information for Business Card

Please consider places on the business card for:

Name
Function (bellow name in smaller size text)

Mobile phone
E-mail
Skype ID
WeChat ID

Adress (3 lines)

Also include the following locations references:
PORTUGAL * DUBAI * HONG KONG

Website: www.rhholdings.example

Requirements
Must have
• Company Logo

```html
<!DOCTYPE html>
<html lang="en">
<head>
<meta charset="utf-8">
<title>Radiant Harbor Holdings – Business Card</title>
<link rel="stylesheet" href="https://fonts.googleapis.com/css2?family=Montserrat:wght@400;500;600&display=swap">
<style>
  :root {
    --page-bg: #e9e6e1;
    --card-dark: #0d0d0e;
    --card-dark-edge: #2a2a2c;
    --card-light: #ffffff;
    --brand-blue: #2aa6df;
    --text-grey: #5d6166;
    --text-soft: #8a8e93;
    --rule: #6f7479;
    --on-dark: #b9bcc0;
  }
  * { box-sizing: border-box; margin: 0; padding: 0; }
  html, body { width: 1200px; height: 900px; overflow: hidden; }
  body {
    background: var(--page-bg);
    font-family: "Montserrat", sans-serif;
    position: relative;
  }
  .card {
    position: absolute;
    left: 250px;
    width: 700px;
    height: 400px;
    border-radius: 26px;
    box-shadow: 0 10px 30px rgba(0,0,0,0.18);
    overflow: hidden;
  }

  /* Back side */
  .card--back {
    top: 30px;
    background: linear-gradient(160deg, var(--card-dark-edge) 0%, var(--card-dark) 45%);
  }
  .back-brand {
    position: absolute;
    top: 130px; left: 0; right: 0;
    display: flex; align-items: center; justify-content: center; gap: 18px;
  }
  .brand-dot {
    width: 22px; height: 22px; border-radius: 50%;
    background: var(--brand-blue);
  }
  .brand-name {
    font-weight: 600;
    color: var(--brand-blue);
    letter-spacing: 2px;
    text-transform: uppercase;
  }
  .back-brand .brand-name { font-size: 34px; }
  .locations {
    position: absolute;
    top: 250px; left: 0; right: 0;
    text-align: center;
    color: var(--on-dark);
    font-size: 17px;
    letter-spacing: 2px;
  }
  .locations .sep { margin: 0 18px; }
  .back-web {
    position: absolute;
    top: 300px; left: 0; right: 0;
    text-align: center;
    color: var(--on-dark);
    font-size: 18px;
    letter-spacing: 0.5px;
  }
  .accent { color: var(--brand-blue); }

  /* Front side */
  .card--front {
    top: 470px;
    background: var(--card-light);
  }
  .holder {
    position: absolute; top: 42px; left: 56px;
  }
  .holder-name { color: var(--brand-blue); font-size: 28px; font-weight: 500; }
  .holder-role { color: var(--text-grey); font-size: 16px; margin-top: 2px; }
  .front-brand {
    position: absolute; top: 92px; right: 50px;
    display: flex; align-items: center; gap: 12px;
  }
  .front-brand .brand-dot { width: 16px; height: 16px; }
  .front-brand .brand-name { font-size: 23px; letter-spacing: 1.5px; }
  .divider {
    position: absolute; top: 176px; left: 0; width: 700px; height: 30px;
  }
  .contacts {
    position: absolute; top: 212px; left: 66px;
    list-style: none;
    color: var(--text-grey);
    font-size: 18px;
  }
  .contacts li {
    display: flex; align-items: center; gap: 16px;
    height: 31px;
  }
  .icon { width: 16px; height: 16px; flex: none; }
  .icon-dot { width: 15px; height: 15px; border-radius: 50%; flex: none; }
  .icon-dot--call { background: var(--brand-blue); }
  .icon-dot--chat { background: #3fae3a; }
  .address {
    position: absolute; top: 284px; left: 438px;
    display: flex; gap: 10px;
    color: var(--text-grey);
    font-size: 17px; line-height: 1.35;
  }
  .address .icon { margin-top: 3px; }
</style>
</head>
<body>

<section class="card card--back" aria-label="Card back">
  <div class="back-brand">
    <span class="brand-dot"></span>
    <span class="brand-name">Radiant Harbor Holdings</span>
  </div>
  <p class="locations">PORTUGAL<span class="sep">•</span>DUBAI<span class="sep">•</span>HONG KONG</p>
  <p class="back-web">www.<span class="accent">rhholdings</span>.example</p>
</section>

<section class="card card--front" aria-label="Card front">
  <div class="holder">
    <p class="holder-name">Your Name</p>
    <p class="holder-role">position</p>
  </div>

  <div class="front-brand">
    <span class="brand-dot"></span>
    <span class="brand-name">Radiant Harbor Holdings</span>
  </div>

  <svg class="divider" viewBox="0 0 700 30" aria-hidden="true">
    <polyline points="0,2 150,2 160,12 170,2 700,2" fill="none" stroke="var(--rule)" stroke-width="1.5"/>
  </svg>

  <ul class="contacts">
    <li>
      <svg class="icon" viewBox="0 0 16 16" aria-hidden="true"><path d="M3 1.5l3 .5 1 3.2-1.8 1.3a9 9 0 0 0 4.3 4.3L10.8 9l3.2 1 .5 3-2 1.5C6.8 14.5 1.5 9.2 1.5 3.5z" fill="var(--text-soft)"/></svg>
      +1 555 014 2277
    </li>
    <li>
      <svg class="icon" viewBox="0 0 16 16" aria-hidden="true"><rect x="1" y="3" width="14" height="10" rx="1" fill="var(--text-soft)"/><polyline points="1.5,3.5 8,9 14.5,3.5" fill="none" stroke="#fff" stroke-width="1.3"/></svg>
      hello@rhholdings.example
    </li>
    <li><span class="icon-dot icon-dot--call"></span>/rhholdings</li>
    <li><span class="icon-dot icon-dot--chat"></span>/rhholdings</li>
    <li>
      <svg class="icon" viewBox="0 0 16 16" aria-hidden="true"><g fill="none" stroke="var(--text-soft)" stroke-width="1.3"><circle cx="8" cy="8" r="6.5"/><ellipse cx="8" cy="8" rx="3" ry="6.5"/><line x1="1.5" y1="8" x2="14.5" y2="8"/></g></svg>
      www.<span class="accent">rhholdings</span>.example
    </li>
  </ul>

  <div class="address">
    <svg class="icon" viewBox="0 0 16 16" aria-hidden="true"><path d="M8 1a5 5 0 0 0-5 5c0 3.8 5 9 5 9s5-5.2 5-9a5 5 0 0 0-5-5zm0 7a2 2 0 1 1 0-4 2 2 0 0 1 0 4z" fill="var(--text-soft)"/></svg>
    <p>Opp. Lantern Point Mall<br>Harbor Jn. Coral Bay<br>Seaview District, India</p>
  </div>
</section>

</body>
</html>
```